Tiko Marsden Systems Web Site

I need website designed for Tiko Marsden Systems, LLC. It is an email marketing software as a service business. I am looking for a five page website with the ability to accept payments. I have included our logo below for integration with the website. I do not have the text ready yet.

The domain to use is tiko-marsden.example

I have also included some examples of other websites that outline the basic structure I would like
https://trybluvoren.example/
https://www.postquill.example/

I know I need to provide some more information, but I want to get the ball rolling and see what is needed.
Thanks!
Owen

```html
<!DOCTYPE html>
<html lang="en">
<head>
<meta charset="utf-8">
<title>Tiko Marsden Systems — Email Marketing Software</title>
<link href="https://fonts.googleapis.com/css2?family=Montserrat:wght@300;400;500;600;700;800&family=Open+Sans:wght@400;600;700&display=swap" rel="stylesheet">
<style>
:root{
  --navy:#221c6b;
  --navy-deep:#1a1558;
  --red:#e9242c;
  --blue:#2d7fe0;
  --ink:#1f1f2e;
  --muted:#77788a;
  --light:#f1f2f5;
  --line:#d9dae2;
  --white:#ffffff;
  --teal:#25b7c4;
  --purple:#7b4fd0;
  --yellow:#f2b632;
  --green:#3cbf6e;
}
*{box-sizing:border-box;margin:0;padding:0}
html,body{width:1200px;height:3076px;overflow:hidden}
body{font-family:"Open Sans",Arial,sans-serif;color:var(--ink);background:var(--white);position:relative}
h1,h2,h3,.nav,.btn,.brand{font-family:"Montserrat",Arial,sans-serif}
.btn{display:inline-block;font-size:11px;font-weight:700;letter-spacing:.5px;text-transform:uppercase;border-radius:20px;padding:9px 20px;text-decoration:none}
.btn-red{background:var(--red);color:var(--white)}
.btn-outline{border:1.5px solid var(--red);color:var(--red);background:var(--white);padding:7px 18px}
.btn-navy{background:var(--navy);color:var(--white)}

/* header */
.site-header{height:88px;display:flex;align-items:center;justify-content:space-between;padding:0 130px 0 140px}
.brand{display:flex;align-items:center;gap:10px;font-weight:700;font-size:17px;color:var(--navy);letter-spacing:.5px}
.brand-dot{width:34px;height:34px;border-radius:50%;border:3px solid var(--blue)}
.nav{display:flex;align-items:center;gap:24px;font-size:11px;font-weight:600;text-transform:uppercase;color:var(--ink)}
.nav a{color:var(--ink);text-decoration:none}
.nav .active{color:var(--red);border-bottom:2px solid var(--red);padding-bottom:3px}
.nav .btn{padding:8px 18px;font-size:10px;color:var(--white)}

/* hero */
.hero{height:452px;background:linear-gradient(180deg,#f7f7f9,#eceef2);position:relative}
.hero-copy{position:absolute;left:140px;top:112px;width:440px}
.hero h1{font-size:31px;line-height:1.28;font-weight:800;color:var(--navy);text-transform:uppercase}
.hero h1 span{color:var(--blue)}
.hero .btn{margin-top:22px}
.hero-art{position:absolute;left:640px;top:20px;width:440px;height:400px;background:
  radial-gradient(ellipse 150px 90px at 58% 72%,#c6cad4 0,rgba(198,202,212,0) 100%),
  radial-gradient(ellipse 200px 150px at 60% 25%,rgba(233,36,44,.35) 0,rgba(243,140,40,.22) 55%,rgba(236,238,242,0) 100%)}
.chev{position:absolute;left:588px;bottom:22px}

/* features */
.features{height:460px;display:flex;justify-content:center;gap:70px;padding-top:72px}
.feature{width:250px;text-align:center}
.feature-icon{width:120px;height:120px;margin:0 auto 18px;border-radius:50%;border:3px solid var(--navy);display:flex;align-items:center;justify-content:center;background:var(--white)}
.feature-icon.soft{border-color:#c9cce0}
.feature h3{font-size:15px;font-weight:700;color:var(--navy);text-transform:uppercase;margin-bottom:8px}
.feature p{font-size:11px;line-height:1.6;color:var(--muted);margin-bottom:18px}

/* about */
.about{height:800px;background:var(--navy);color:var(--white);text-align:center;padding-top:72px;position:relative}
.section-title{font-size:34px;font-weight:300;text-transform:uppercase;letter-spacing:1px}
.section-title b{font-weight:700}
.rule{display:block;margin:10px auto 0}
.about p{width:860px;margin:22px auto 0;font-size:12px;line-height:1.75;color:#d6d5ea}
.about p strong{color:var(--white);font-weight:600;font-size:14px}
.app-shot{width:680px;height:400px;margin:40px auto 0;background:var(--white);border-radius:6px;overflow:hidden;box-shadow:0 16px 40px rgba(0,0,0,.35);text-align:left;color:var(--ink);position:relative}
.app-bar{height:22px;background:#f1f1f4;display:flex;align-items:center;gap:6px;padding-left:12px}
.app-bar i{width:8px;height:8px;border-radius:50%;background:#e65a5a}
.app-bar i:nth-child(2){background:#f1bc3d}.app-bar i:nth-child(3){background:#52c35b}
.app-tools{display:flex;gap:10px;padding:16px 22px 0;justify-content:center}
.tool{width:68px;text-align:center;font-size:8px;font-weight:600;text-transform:uppercase;color:var(--muted)}
.tool span{display:flex;align-items:center;justify-content:center;height:46px;border-radius:3px;margin-bottom:4px}
.tool span b{width:18px;height:14px;border:2px solid var(--white);border-radius:2px}
.template{width:400px;margin:14px auto 0;background:#f4f6fb;border:1px solid var(--line)}
.template-head{height:22px;background:var(--blue);color:var(--white);font-size:9px;font-weight:600;display:flex;align-items:center;justify-content:center}
.template-photo{height:110px;background:linear-gradient(135deg,#9fb3cf,#d7dee9 60%,#b8c6d8)}
.template-body{padding:10px 14px;display:flex;justify-content:space-between;align-items:flex-end}
.template-body h4{font-size:10px;font-weight:700;margin-bottom:4px}
.template-body p{width:auto;margin:0;font-size:8px;line-height:1.5;color:var(--muted)}
.template-body .btn{margin:0;font-size:7px;padding:4px 10px;border-width:1px}
.player{position:absolute;left:0;right:0;bottom:0;height:26px;background:#2a2a35;display:flex;align-items:center;gap:10px;padding:0 12px}
.player .track{flex:1;height:4px;background:#55555f;border-radius:2px;position:relative}
.player .track i{position:absolute;left:0;top:0;bottom:0;width:38%;background:var(--blue);border-radius:2px}
.about .btn{margin-top:40px}

/* product features */
.product{height:560px;background:linear-gradient(180deg,#eef0f4,#f6f7f9);text-align:center;padding-top:66px}
.product .section-title{color:var(--navy)}
.product-grid{display:flex;justify-content:center;gap:40px;margin-top:44px}
.product-item{width:200px}
.product-icon{width:120px;height:120px;margin:0 auto 16px;border-radius:50%;border:3px solid var(--navy);background:radial-gradient(circle at 50% 60%,#3b6fd0 0,#8fb0e6 38%,#eef2fa 70%)}
.product-item:nth-child(2) .product-icon{background:radial-gradient(circle at 50% 60%,#3b5fa8 0,#b8cbe9 42%,#f2f5fb 70%)}
.product-item:nth-child(3) .product-icon{border-color:#d0d4e2;background:radial-gradient(circle at 50% 55%,#7dc4b0 0,#e9dca8 42%,#f6f7f9 70%)}
.product-item:nth-child(4) .product-icon{background:radial-gradient(circle at 50% 55%,#2a2a35 0,#8a8d99 32%,#f0d6d6 55%,#f6f7f9 72%)}
.product-item h3{font-size:14px;font-weight:700;line-height:1.3;color:var(--ink);margin-bottom:8px}
.product-item:first-child h3{color:var(--red)}
.product-item p{font-size:11px;line-height:1.6;color:var(--muted)}

/* reviews */
.reviews{height:420px;text-align:center;padding-top:56px;position:relative}
.reviews .section-title{color:var(--navy)}
.review-row{display:flex;justify-content:center;gap:40px;margin-top:40px}
.review{width:440px;text-align:left}
.review blockquote{font-size:12px;line-height:1.7;color:var(--muted);position:relative;padding-left:24px}
.review blockquote::before{content:"\201C";position:absolute;left:0;top:-8px;font-size:34px;color:var(--navy);font-family:Georgia,serif}
.reviewer{display:flex;align-items:center;gap:12px;margin-top:18px;padding-left:24px;font-size:12px;font-weight:600;color:var(--ink)}
.avatar{width:38px;height:38px;border-radius:50%;background:linear-gradient(135deg,#c9cfe0,#8f98b5)}
.arrow{position:absolute;top:236px}
.arrow-left{left:60px}.arrow-right{right:60px}

/* footer */
.site-footer{height:296px;background:var(--navy-deep);color:#cfcde6;position:relative}
.footer-cols{display:flex;padding:46px 0 0 140px;gap:60px;font-size:11px}
.footer-cols h4{font-family:"Montserrat",Arial,sans-serif;font-size:12px;font-weight:700;color:var(--white);text-transform:uppercase;margin-bottom:14px}
.footer-cols ul{list-style:none;line-height:2}
.footer-cols ul li:first-child{color:var(--blue)}
.contact li{display:flex;gap:8px;align-items:center;line-height:1.5;margin-bottom:8px}
.question h4{font-size:15px;text-transform:none}
.question input{display:block;width:250px;height:26px;margin-bottom:10px;border:none;border-radius:2px;padding:0 10px;font-size:10px;color:var(--muted)}
.question .btn{padding:7px 18px;font-size:10px;border:none}
.footer-brand{position:absolute;right:110px;top:64px;display:flex;flex-direction:column;align-items:center;gap:14px;font-family:"Montserrat",Arial,sans-serif;font-weight:700;font-size:20px;color:var(--white);letter-spacing:1px}
.footer-brand .ring{width:86px;height:86px;border-radius:50%;border:3px solid var(--white)}
.footer-bottom{position:absolute;left:0;right:0;bottom:0;height:40px;background:#141048;display:flex;justify-content:space-between;align-items:center;padding:0 140px;font-size:10px;color:#a9a6cc}
.socials{display:flex;gap:8px}
.socials i{width:20px;height:20px;border-radius:50%;background:#3a3585}
</style>
</head>
<body>

<header class="site-header">
  <div class="brand"><span class="brand-dot"></span>TIKO MARSDEN</div>
  <nav class="nav">
    <a class="active" href="#">Home</a>
    <a href="#">About us</a>
    <a href="#">Services</a>
    <a href="#">Plans &amp; Pricing</a>
    <a href="#">FAQs</a>
    <a class="btn btn-navy" href="#">Login</a>
    <a class="btn btn-red" href="#">Sign up</a>
  </nav>
</header>

<section class="hero">
  <div class="hero-copy">
    <h1>We are an <span>email marketing software</span> as a service business.</h1>
    <a class="btn btn-red" href="#">Sign up for free &rsaquo;</a>
  </div>
  <div class="hero-art" role="img" aria-label="Illustration of a laptop with a burst of red and orange envelopes flying out of the screen"></div>
  <svg class="chev" width="24" height="14" viewBox="0 0 24 14"><path d="M2 2l10 9 10-9" fill="none" stroke="#9aa0b4" stroke-width="2.5"/></svg>
</section>

<section class="features">
  <div class="feature">
    <div class="feature-icon">
      <svg width="64" height="52" viewBox="0 0 64 52"><rect x="2" y="2" width="60" height="48" rx="3" fill="none" stroke="#221c6b" stroke-width="3"/><line x1="2" y1="12" x2="62" y2="12" stroke="#221c6b" stroke-width="3"/><rect x="14" y="20" width="36" height="24" fill="#e9242c"/><path d="M14 20l18 13 18-13" fill="none" stroke="#fff" stroke-width="2"/></svg>
    </div>
    <h3>Simple Interface</h3>
    <p>Lorem ipsum dolor sit amet, consectetur adipiscing elit, sed diam nonummy aliquam erat volutpat.</p>
    <a class="btn btn-outline" href="#">See features &rsaquo;</a>
  </div>
  <div class="feature">
    <div class="feature-icon soft">
      <svg width="56" height="56" viewBox="0 0 56 56"><path d="M28 4h22v22L26 50 4 28z" fill="none" stroke="#2d7fe0" stroke-width="3" stroke-linejoin="round"/><circle cx="40" cy="14" r="4" fill="none" stroke="#2d7fe0" stroke-width="3"/><circle cx="27" cy="28" r="8" fill="#e9242c"/><text x="27" y="32" text-anchor="middle" font-family="Montserrat,sans-serif" font-size="11" font-weight="700" fill="#fff">$</text></svg>
    </div>
    <h3>Affordable Pricing</h3>
    <p>Lorem ipsum dolor sit amet, consectetur adipiscing elit, sed diam nonummy aliquam erat volutpat.</p>
    <a class="btn btn-outline" href="#">See plans &amp; pricing &rsaquo;</a>
  </div>
  <div class="feature">
    <div class="feature-icon soft">
      <svg width="60" height="52" viewBox="0 0 60 52"><path d="M6 4h48a4 4 0 014 4v26a4 4 0 01-4 4H24l-12 10v-10H6a4 4 0 01-4-4V8a4 4 0 014-4z" fill="none" stroke="#2d7fe0" stroke-width="3" stroke-linejoin="round"/><path d="M20 21l7 7 13-13" fill="none" stroke="#e9242c" stroke-width="3.5" stroke-linecap="round" stroke-linejoin="round"/></svg>
    </div>
    <h3>Responsive Support</h3>
    <p>Lorem ipsum dolor sit amet, consectetur adipiscing elit, sed diam nonummy aliquam erat volutpat.</p>
    <a class="btn btn-outline" href="#">Any question? &rsaquo;</a>
  </div>
</section>

<section class="about">
  <h2 class="section-title">About <b>Tiko Marsden</b></h2>
  <svg class="rule" width="140" height="12" viewBox="0 0 140 12"><line x1="0" y1="6" x2="60" y2="6" stroke="#6f6aa8"/><circle cx="70" cy="6" r="5" fill="none" stroke="#6f6aa8"/><line x1="80" y1="6" x2="140" y2="6" stroke="#6f6aa8"/></svg>
  <p><strong>Duis autem vel eum iriure dolor in hendrerit in vulputate velit esse molestie consequat, vel illum dolore eu facilisis.</strong><br>
  Lorem ipsum dolor sit amet, consectetuer adipiscing elit, sed diam nonummy nibh euismod tincidunt ut laoreet dolore magna aliquam erat volutpat. Ut wisi enim ad minim veniam, quis nostrud exerci tation ullamcorper suscipit lobortis.</p>
  <div class="app-shot">
    <div class="app-bar"><i></i><i></i><i></i></div>
    <div class="app-tools">
      <div class="tool"><span style="background:var(--teal)"><b></b></span>Inbox</div>
      <div class="tool"><span style="background:var(--purple)"><b></b></span>Lists</div>
      <div class="tool"><span style="background:var(--yellow)"><b></b></span>Forms</div>
      <div class="tool"><span style="background:var(--blue)"><b></b></span>Editor</div>
      <div class="tool"><span style="background:var(--green)"><b></b></span>Reports</div>
      <div class="tool"><span style="background:var(--purple)"><b></b></span>Share</div>
      <div class="tool"><span style="background:var(--blue)"><b></b></span>Tools</div>
      <div class="tool"><span style="background:var(--teal)"><b></b></span>Contacts</div>
    </div>
    <div class="template">
      <div class="template-head">Your Company Logo</div>
      <div class="template-photo" role="img" aria-label="Newsletter header photo"></div>
      <div class="template-body">
        <div>
          <h4>Lorem ipsum dolor sit amet, consectetur</h4>
          <p>Sed diam nonummy nibh euismod tincidunt ut<br>laoreet dolore magna aliquam erat volutpat.</p>
        </div>
        <a class="btn btn-outline" href="#">Any question?</a>
      </div>
    </div>
    <div class="player">
      <svg width="10" height="10" viewBox="0 0 10 10"><path d="M1 0l8 5-8 5z" fill="#fff"/></svg>
      <div class="track"><i></i></div>
      <svg width="12" height="10" viewBox="0 0 12 10"><path d="M1 3h3l3-3v10L4 7H1z" fill="#fff"/></svg>
    </div>
  </div>
  <a class="btn btn-red" href="#">Try it for free &rsaquo;</a>
</section>

<section class="product">
  <h2 class="section-title">Product <b>Features</b></h2>
  <svg class="rule" width="140" height="12" viewBox="0 0 140 12"><line x1="0" y1="6" x2="60" y2="6" stroke="#b7b9c8"/><circle cx="70" cy="6" r="5" fill="none" stroke="#b7b9c8"/><line x1="80" y1="6" x2="140" y2="6" stroke="#b7b9c8"/></svg>
  <div class="product-grid">
    <div class="product-item">
      <div class="product-icon" role="img" aria-label="Illustration of an email campaign window with envelopes"></div>
      <h3>Create Email Campaigns</h3>
      <p>Lorem Ipsum is simply dummy text of the printing and industry.</p>
    </div>
    <div class="product-item">
      <div class="product-icon" role="img" aria-label="Illustration of a person working on an automated email schedule"></div>
      <h3>Use Automated Email Schedules</h3>
      <p>Lorem Ipsum is simply dummy text of the printing and industry.</p>
    </div>
    <div class="product-item">
      <div class="product-icon" role="img" aria-label="Illustration of two campaign variants compared side by side"></div>
      <h3>A/B Test Your Campaigns</h3>
      <p>Lorem Ipsum is simply dummy text of the printing and industry.</p>
    </div>
    <div class="product-item">
      <div class="product-icon" role="img" aria-label="Illustration of a phone showing a deliverability check"></div>
      <h3>Text Your Emails for Deliverability Score</h3>
      <p>Lorem Ipsum is simply dummy text of the printing and industry.</p>
    </div>
  </div>
</section>

<section class="reviews">
  <h2 class="section-title">Client <b>Reviews</b></h2>
  <svg class="rule" width="140" height="12" viewBox="0 0 140 12"><line x1="0" y1="6" x2="60" y2="6" stroke="#b7b9c8"/><circle cx="70" cy="6" r="5" fill="none" stroke="#b7b9c8"/><line x1="80" y1="6" x2="140" y2="6" stroke="#b7b9c8"/></svg>
  <svg class="arrow arrow-left" width="14" height="26" viewBox="0 0 14 26"><path d="M12 2L2 13l10 11" fill="none" stroke="#b7b9c8" stroke-width="2"/></svg>
  <svg class="arrow arrow-right" width="14" height="26" viewBox="0 0 14 26"><path d="M2 2l10 11L2 24" fill="none" stroke="#b7b9c8" stroke-width="2"/></svg>
  <div class="review-row">
    <div class="review">
      <blockquote>Lorem ipsum dolor sit amet, consectetur adipiscing elit. Sed do eiusmod tempor incididunt ut labore et dolore magna aliqua, quis nostrud exercitation.</blockquote>
      <div class="reviewer"><span class="avatar" role="img" aria-label="Client portrait"></span>Rafe Dalton Okoro</div>
    </div>
    <div class="review">
      <blockquote>Lorem ipsum dolor sit amet, consectetur adipiscing elit. Sed do eiusmod tempor incididunt ut labore et dolore magna aliqua, quis nostrud exercitation.</blockquote>
      <div class="reviewer"><span class="avatar" role="img" aria-label="Client portrait"></span>Mr. Ivo Pennick</div>
    </div>
  </div>
</section>

<footer class="site-footer">
  <div class="footer-cols">
    <div>
      <h4>Quick Links</h4>
      <ul><li>Home</li><li>About us</li><li>Services</li><li>Plans &amp; Pricing</li><li>FAQs</li></ul>
    </div>
    <div class="contact">
      <h4>Contact us</h4>
      <ul>
        <li><svg width="12" height="14" viewBox="0 0 12 14"><path d="M6 13s5-5 5-8A5 5 0 001 5c0 3 5 8 5 8z" fill="none" stroke="#fff"/><circle cx="6" cy="5" r="1.6" fill="#fff"/></svg>Tiko Marsden, 120 Elm Street<br>Fairhaven, Country</li>
        <li><svg width="12" height="12" viewBox="0 0 12 12"><path d="M2 1h3l1 3-2 1a7 7 0 003 3l1-2 3 1v3c-6 0-10-4-10-10z" fill="#fff"/></svg>555 010 2040</li>
        <li><svg width="12" height="10" viewBox="0 0 12 10"><rect x=".5" y=".5" width="11" height="9" fill="none" stroke="#fff"/><path d="M1 1l5 4 5-4" fill="none" stroke="#fff"/></svg>info@tiko-marsden.example</li>
      </ul>
    </div>
    <div class="question">
      <h4>Do You Have A Question?</h4>
      <input type="text" value="Enter email">
      <input type="text" value="Enter question">
      <a class="btn btn-red" href="#">Submit</a>
    </div>
  </div>
  <div class="footer-brand"><span class="ring"></span>TIKO MARSDEN</div>
  <div class="footer-bottom">
    <span>Copyright &copy; 2018 Tiko Marsden Systems. All Rights Reserved.</span>
    <div class="socials"><i></i><i></i><i></i><i></i><i></i></div>
  </div>
</footer>

</body>
</html>
```